Webdesign für Anbieter von Erotik-Geschichten
Zielgruppe
Wir sind ein Anbieter von Erotik-Geschichten. Die Marke heisst Lunvo Erotica. Das Erlebnis für die Kunden soll hochwertig und persönlich wirken. Daher in keiner Art und Weise schmuddelig. Die Zielgruppe sind Frauen ab ca. 20-40. Die Geschichten werden frei lesbar sein, d.h. es ist kein Online-Shop sondern mehr eine Art Blog mit verschiedenen Geschichten.
Aufgabenstellung
Wichtig ist uns eine schlichtes, minimalistisches Design (vrgl. Tafelwerk) aber trotzdem hochwertig (leicht luxuriös) wirkend.

```html
<!DOCTYPE html>
<html lang="de">
<head>
<meta charset="utf-8">
<title>Lunvo – Kategorien</title>
<link href="https://fonts.googleapis.com/css2?family=Bitter:wght@400;600;700&family=Open+Sans:wght@400;600&display=swap" rel="stylesheet">
<style>
  :root {
    --red: #e0251b;
    --ink: #2b2b2b;
    --muted: #8a8a8a;
    --bg: #ffffff;
  }
  * { margin: 0; padding: 0; box-sizing: border-box; }
  html, body { width: 803px; height: 1200px; overflow: hidden; background: var(--bg); }
  body { position: relative; font-family: "Bitter", serif; color: var(--ink); }
  a { color: inherit; text-decoration: none; }

  .brand { position: absolute; font-family: "Bitter", serif; font-weight: 600; color: var(--ink); letter-spacing: 0.5px; }
  .brand--header { left: 45px; top: 24px; font-size: 26px; }
  .brand--footer { left: 0; width: 803px; text-align: center; top: 1116px; font-size: 34px; }

  .main-nav { position: absolute; top: 35px; left: 169px; display: flex; gap: 0; font-size: 9.5px; letter-spacing: 0.6px; }
  .main-nav a { position: absolute; white-space: nowrap; }
  .main-nav .active { color: var(--red); font-weight: 700; }

  .tools { position: absolute; top: 33px; left: 560px; }
  .tools svg { position: absolute; fill: var(--red); }

  .upgrade {
    position: absolute; left: 637px; top: 29px; width: 77px; height: 23px;
    border: 1.5px solid var(--red); border-radius: 12px; color: var(--red);
    font-weight: 700; font-size: 10px; display: flex; align-items: center; justify-content: center;
  }
  .avatar { position: absolute; left: 725px; top: 29px; width: 25px; height: 25px; border-radius: 50%;
    border: 1.5px solid var(--red); background: radial-gradient(circle at 50% 45%, #b57a5c, #4a2a1e 70%); }

  .page-title { position: absolute; left: 167px; top: 118px; font-size: 44px; font-weight: 400; color: var(--red); letter-spacing: 0.5px; }

  .breadcrumb { position: absolute; left: 169px; top: 195px; font-family: "Open Sans", sans-serif; font-size: 8.5px; color: var(--muted); }
  .breadcrumb a, .breadcrumb span { position: absolute; white-space: nowrap; }
  .breadcrumb a { text-decoration: underline; }
  .breadcrumb .sep { color: var(--red); }

  .category { position: absolute; width: 132px; }
  .category .photo { width: 132px; height: 175px; }
  .category h2 { position: absolute; top: 186px; font-size: 17.5px; font-weight: 400; letter-spacing: 0.6px; white-space: nowrap; }

  .load-more {
    position: absolute; left: 279px; top: 970px; width: 244px; height: 29px;
    border: 2px solid var(--ink); border-radius: 15px;
    display: flex; align-items: center; justify-content: center;
    font-size: 12.5px; font-weight: 700; letter-spacing: 0.4px;
  }

  .site-footer { position: absolute; left: 0; top: 1075px; width: 803px; height: 125px; border-top: 1px solid var(--red); }
  .footer-nav a { position: absolute; top: 12px; font-size: 9.5px; letter-spacing: 0.6px; white-space: nowrap; }
  .legal { position: absolute; top: 108px; font-family: "Open Sans", sans-serif; font-size: 7px; font-weight: 600; color: var(--muted); white-space: nowrap; }
  .legal.link { text-decoration: underline; }
</style>
</head>
<body>

<header>
  <a class="brand brand--header" href="#">Lunvo</a>
  <nav class="main-nav">
    <a href="#" style="left:0">HOME</a>
    <a href="#" class="active" style="left:52px">KATEGORIEN</a>
    <a href="#" style="left:137px">AUTOREN</a>
    <a href="#" style="left:206px">ÜBER UNS</a>
  </nav>
  <div class="tools">
    <svg style="left:2px;top:2px" width="11" height="11" viewBox="0 0 11 11" aria-label="Suche"><circle cx="4.5" cy="4.5" r="3.3" fill="none" stroke="#e0251b" stroke-width="1.8"/><path d="M7 7l3 3" stroke="#e0251b" stroke-width="2" stroke-linecap="round"/></svg>
    <svg style="left:29px;top:2px" width="8" height="11" viewBox="0 0 8 11" aria-label="Merkliste"><path d="M0 0h8v11L4 8 0 11z"/></svg>
    <svg style="left:53px;top:2px" width="10" height="11" viewBox="0 0 10 11" aria-label="Benachrichtigungen"><path d="M5 0C2.6 0 1.6 2 1.6 4v2.5L0 8.5h10L8.4 6.5V4C8.4 2 7.4 0 5 0z"/><circle cx="5" cy="9.8" r="1.2"/></svg>
  </div>
  <a class="upgrade" href="#">Upgrade</a>
  <div class="avatar" role="img" aria-label="Profilbild"></div>
</header>

<main>
  <h1 class="page-title">Kategorien</h1>

  <nav class="breadcrumb">
    <a href="#" style="left:0">Start</a>
    <span class="sep" style="left:27px">&gt;</span>
    <a href="#" style="left:42px">Kategorien</a>
    <span class="sep" style="left:93px">&gt;</span>
    <a href="#" style="left:108px">BDSM</a>
    <span class="sep" style="left:137px">&gt;</span>
    <span style="left:152px">Zufälle und Konsequenzen</span>
  </nav>

  <article class="category" style="left:170px;top:227px">
    <div class="photo" role="img" aria-label="Foto: Hüfte mit weißem Slip" style="background:linear-gradient(135deg,#f1ddd0,#d9b39c 60%,#eee)"></div>
    <h2 style="left:-1px">Alleine</h2>
  </article>
  <article class="category" style="left:332px;top:227px">
    <div class="photo" role="img" aria-label="Foto: Paar im hellen Büro am Laptop" style="background:linear-gradient(160deg,#f2f2f0,#c9c9c6 55%,#8f939a)"></div>
    <h2 style="left:2px">Arbeitsplatz</h2>
  </article>
  <article class="category" style="left:494px;top:227px">
    <div class="photo" role="img" aria-label="Foto: Hände vor graugrünem Hintergrund" style="background:linear-gradient(160deg,#a9b5b3,#cfb39e 50%,#9aa6a3)"></div>
    <h2 style="left:4px">Schule</h2>
  </article>

  <article class="category" style="left:170px;top:473px">
    <div class="photo" role="img" aria-label="Foto: sich küssendes Paar" style="background:linear-gradient(150deg,#ece8e4,#a8765a 50%,#6b4332)"></div>
    <h2 style="left:-1px">Ferien</h2>
  </article>
  <article class="category" style="left:332px;top:473px">
    <div class="photo" role="img" aria-label="Foto: Handgelenk mit Lederfessel" style="background:linear-gradient(120deg,#1c1715,#7a3d22 55%,#c07a4a)"></div>
    <h2 style="left:2px">BDSM</h2>
  </article>
  <article class="category" style="left:494px;top:473px">
    <div class="photo" role="img" aria-label="Foto: Füße unter weißer Bettdecke" style="background:linear-gradient(160deg,#e6e7ea,#d5b8a4 50%,#e9eaed)"></div>
    <h2 style="left:4px">Dreier</h2>
  </article>

  <article class="category" style="left:170px;top:719px">
    <div class="photo" role="img" aria-label="Foto: zwei sich küssende Frauen" style="background:linear-gradient(130deg,#111512,#3a2a22 45%,#b98b6e 75%,#2a2320)"></div>
    <h2 style="left:-1px">Lesbisch</h2>
  </article>
  <article class="category" style="left:332px;top:719px">
    <div class="photo" role="img" aria-label="Foto: Frau geht auf Mann im Bett zu" style="background:linear-gradient(170deg,#d8d2cc,#ecebe8 50%,#b59a87)"></div>
    <h2 style="left:2px">Sugar/Escort</h2>
  </article>
  <article class="category" style="left:494px;top:719px">
    <div class="photo" role="img" aria-label="Foto: Frau liegt auf weißem Kissen" style="background:linear-gradient(160deg,#e7dcd2,#d9b9a3 45%,#f4f3f1)"></div>
    <h2 style="left:4px">Step</h2>
  </article>

  <a class="load-more" href="#">Mehr Kategorien laden</a>
</main>

<footer class="site-footer">
  <nav class="footer-nav">
    <a href="#" style="left:271px">HOME</a>
    <a href="#" style="left:323px">KATEGORIEN</a>
    <a href="#" style="left:408px">AUTOREN</a>
    <a href="#" style="left:477px">ÜBER UNS</a>
  </nav>
  <span class="legal" style="left:243px">© Lunvo GmbH 2021</span>
  <a class="legal link" href="#" style="left:358px">Impressum</a>
  <a class="legal link" href="#" style="left:442px">AGB</a>
  <a class="legal link" href="#" style="left:497px">Datenschutz</a>
</footer>
<a class="brand brand--footer" href="#">Lunvo</a>

</body>
</html>
```